Modern card design needed for building development company

We are looking for a sharp modern new look for our business cards.
We are a New Zealand based company called TKR Ventures NZ LTD that specialises in subdividing large sections, housing and commercial buildings.
We have attached a photo of the current logo and would like to see it improved somehow as it looks a bit dated.
We are open to any colours.

Target Market(s)

Investors, Property buyers

Industry/Entity Type

Investment

Contact Information for Business Card

TKR VENTURES NZ LTD
www.tkrventuresnz.example.nz

Dorian Fletcher
Phone +64 21 843 209
Email dpfletcher@mailvane.example.nz

Font styles to use
Serif
Sans Serif

Colors
0792cd
33a6d7
85cae6
6b449b
886aae
f04a50
ec1f27
f37122
f68d4d

Requirements
Must have
• Please try and make the logo more modern or if you have a similar one we would like to see it.

```html
<!DOCTYPE html>
<html lang="en">
<head>
<meta charset="utf-8">
<title>TKR Ventures NZ LTD – Business Card</title>
<link rel="stylesheet" href="https://fonts.googleapis.com/css2?family=Cinzel:wght@500&family=Archivo:wght@400;700&display=swap">
<style>
  :root {
    --stage: #1c1c1e;
    --brand-red: #961c2c;
    --brand-red-dark: #7e1523;
    --paper: #ffffff;
    --paper-shade: #ececec;
    --ink-light: #ffffff;
  }
  * { box-sizing: border-box; margin: 0; padding: 0; }
  html, body { width: 1200px; height: 963px; overflow: hidden; }
  body {
    background: var(--stage);
    display: flex;
    align-items: center;
    justify-content: center;
    gap: 40px;
    font-family: "Archivo", sans-serif;
  }
  .card {
    position: relative;
    width: 540px;
    height: 308px;
    border-radius: 14px;
    overflow: hidden;
  }
  /* Front */
  .card--front { background: var(--brand-red); color: var(--ink-light); }
  .wordmark {
    font-family: "Cinzel", serif;
    font-weight: 500;
    display: flex;
    align-items: center;
    gap: 10px;
    white-space: nowrap;
  }
  .wordmark__square { width: 12px; height: 12px; flex: none; }
  .card--front .wordmark {
    position: absolute;
    left: 34px;
    top: 112px;
    font-size: 19px;
    letter-spacing: 0.5px;
    color: var(--ink-light);
  }
  .card--front .wordmark__square { background: var(--ink-light); }
  .divider {
    position: absolute;
    left: 282px;
    top: 70px;
    width: 1px;
    height: 120px;
    background: rgba(255,255,255,0.75);
  }
  .contact {
    position: absolute;
    left: 304px;
    top: 90px;
  }
  .contact__name {
    font-weight: 700;
    font-size: 21px;
    letter-spacing: 0.3px;
    text-transform: uppercase;
    margin-bottom: 10px;
  }
  .contact__line {
    display: flex;
    align-items: center;
    gap: 8px;
    font-size: 12.5px;
    line-height: 20px;
  }
  .contact__icon { width: 11px; height: 11px; flex: none; }
  .web-band {
    position: absolute;
    right: 0;
    bottom: 0;
    width: 310px;
    height: 34px;
    background: var(--paper);
    clip-path: polygon(26px 0, 100% 0, 100% 100%, 0 100%);
    display: flex;
    align-items: center;
    justify-content: flex-end;
    padding-right: 22px;
    color: var(--brand-red);
    font-size: 13px;
  }
  /* Back */
  .card--back {
    background: linear-gradient(135deg, var(--paper) 55%, var(--paper-shade));
    display: flex;
    align-items: center;
    justify-content: center;
  }
  .card--back .wordmark { font-size: 28px; color: var(--brand-red); }
  .card--back .wordmark__square { width: 16px; height: 16px; background: var(--brand-red); }
</style>
</head>
<body>
  <section class="card card--front" aria-label="Business card front">
    <div class="wordmark">
      <span class="wordmark__square"></span>
      <span>TKR Ventures NZ LTD</span>
    </div>
    <div class="divider"></div>
    <div class="contact">
      <p class="contact__name">Dorian Fletcher</p>
      <p class="contact__line">
        <svg class="contact__icon" viewBox="0 0 24 24" aria-hidden="true"><path fill="#fff" d="M6.6 10.8a15.1 15.1 0 0 0 6.6 6.6l2.2-2.2a1 1 0 0 1 1-.25 11.4 11.4 0 0 0 3.6.57 1 1 0 0 1 1 1V20a1 1 0 0 1-1 1A17 17 0 0 1 3 4a1 1 0 0 1 1-1h3.5a1 1 0 0 1 1 1c0 1.25.2 2.45.57 3.57a1 1 0 0 1-.25 1z"/></svg>
        +64 21 843 209
      </p>
      <p class="contact__line">
        <svg class="contact__icon" viewBox="0 0 24 24" aria-hidden="true"><rect x="2" y="5" width="20" height="14" rx="1.5" fill="none" stroke="#fff" stroke-width="2"/><path d="M2.5 6l9.5 7 9.5-7" fill="none" stroke="#fff" stroke-width="2"/></svg>
        dpfletcher@mailvane.example.nz
      </p>
    </div>
    <div class="web-band">www.tkrventuresnz.example.nz</div>
  </section>

  <section class="card card--back" aria-label="Business card back">
    <div class="wordmark">
      <span class="wordmark__square"></span>
      <span>TKR Ventures NZ LTD</span>
    </div>
  </section>
</body>
</html>
```